Business Card Design- Mortgage Firm

Looking to design a business Card for our Outside sales people. This card is used to provide their contact information to prospective clients and realtors. Must have All Pertinent company and licensing information by law. We are looking for a very modern design that flows with our current logo color scheme. Red/White/Black

Industry/Entity Type

Mortgage Lender

Contact Information for Business Card

Must stick with current color scheme.

Colors
f04a50
ffffff
ecf7fb

Requirements
Must have
• Company Logo or similar
• Company Address (748 W Alder Avenue, Suite 312, Bellmont CA 92879 NMLS: 4072916)
• Agent Name (Mira Talbot)
• Title (Senior Mortgage Loan Originator)
• NMLS# 8395021
• Toll Free: 800-627-3184
• Direct : 310-555-4860
Nice to have
• Room for Agent Picture

```html
<!DOCTYPE html>
<html lang="en">
<head>
<meta charset="utf-8">
<title>Crestline Mortgage – Business Card</title>
<link rel="stylesheet" href="https://fonts.googleapis.com/css2?family=Open+Sans:wght@400;700&display=swap">
<style>
  :root {
    --card-bg: #ecf7fb;
    --brand-red: #b72126;
    --ink: #111111;
    --rule: #1a1a1a;
  }
  html, body {
    margin: 0;
    padding: 0;
    width: 706px;
    height: 1200px;
    overflow: hidden;
    background: #ffffff;
  }
  .card {
    position: relative;
    width: 706px;
    height: 1200px;
    background: var(--card-bg);
    font-family: "Open Sans", Arial, sans-serif;
    color: var(--ink);
    overflow: hidden;
  }
  .band {
    position: absolute;
    left: 0;
    width: 706px;
  }
  .band-dark-top { top: 0; height: 70px; background: var(--ink); }
  .band-red-top { top: 92px; height: 34px; background: var(--brand-red); }
  .band-red-bottom { bottom: 92px; height: 34px; background: var(--brand-red); }
  .band-dark-bottom { bottom: 0; height: 70px; background: var(--ink); }
  .brand {
    position: absolute;
    top: 303px;
    left: 0;
    width: 706px;
    display: flex;
    justify-content: center;
    align-items: center;
    gap: 14px;
  }
  .brand-square {
    width: 34px;
    height: 34px;
    background: var(--brand-red);
  }
  .brand-name {
    font-weight: 700;
    font-size: 33px;
    letter-spacing: 1.5px;
    color: var(--brand-red);
    text-transform: uppercase;
    line-height: 1;
  }
  .rule {
    position: absolute;
    left: 69px;
    width: 570px;
    height: 0;
    border-top: 2px solid var(--rule);
  }
  .rule-top { top: 430px; }
  .rule-bottom { top: 638px; }
  .agent {
    position: absolute;
    top: 492px;
    left: 0;
    width: 706px;
    text-align: center;
  }
  .agent-name {
    margin: 0;
    font-weight: 700;
    font-size: 31px;
    line-height: 40px;
    color: var(--brand-red);
  }
  .agent-title {
    margin: 0;
    font-size: 24px;
    line-height: 32px;
  }
  .contact {
    position: absolute;
    top: 713px;
    left: 0;
    width: 706px;
    text-align: center;
    font-size: 23px;
    line-height: 33px;
  }
  .contact p { margin: 0; }
  .contact .agent-license { margin-bottom: 13px; }
  .contact .company-license { margin-bottom: 6px; }
</style>
</head>
<body>
  <main class="card">
    <div class="band band-dark-top"></div>
    <div class="band band-red-top"></div>

    <header class="brand">
      <span class="brand-square"></span>
      <span class="brand-name">Crestline Mortgage</span>
    </header>

    <div class="rule rule-top"></div>

    <section class="agent">
      <h1 class="agent-name">Mira Talbot</h1>
      <p class="agent-title">Senior Mortgage Loan Originator</p>
    </section>

    <div class="rule rule-bottom"></div>

    <section class="contact">
      <p class="agent-license">NMLS: 8395021</p>
      <p>748 W Alder Avenue, Suite 312</p>
      <p>Bellmont CA 92879</p>
      <p class="company-license">NMLS: 4072916</p>
      <p>Toll Free: 800-627-3184</p>
      <p>Direct: 310-555-4860</p>
    </section>

    <div class="band band-red-bottom"></div>
    <div class="band band-dark-bottom"></div>
  </main>
</body>
</html>
```